Creative Real Estate Listing Mailer

I would like a creative double sided Real Estate listing flier/mailer to send out enticing people to list their house for sale with me. An example in my head, but feel free to be creative,.. would be one side with a Weiner dog with a sack of money on its back saying something like " its time to cash in" and the other side having some kind of southwest backdrop ( I live in Arizona) or luxury home, with my photo and my contact info saying something like list your house with me, or see what your home is worth etc.

Target Market(s)

People interested in selling their homes

Industry/Entity Type

Real Estate Agent

Contact Information for Business Card

Similar to the flyer, but simpler

Requirements
Must have
• My name: Brent Holloway
My Email: brentholloway@mailvista.net
My Phone# (480) 317 4926
Website www.Brentholloway.com

```html
<!DOCTYPE html>
<html lang="en">
<head>
<meta charset="utf-8">
<title>Brent Holloway – Real Estate Mailer</title>
<link href="https://fonts.googleapis.com/css2?family=Oswald:wght@300;400;600&family=Open+Sans:wght@400;600&display=swap" rel="stylesheet">
<style>
  :root{
    --navy:#0c4a70;
    --navy-deep:#083a59;
    --white:#ffffff;
    --stage:#2c2e33;
    --ink:#1c2a36;
    --accent:#b7322a;
  }
  *{box-sizing:border-box;margin:0;padding:0}
  html,body{width:1200px;height:1200px;overflow:hidden;background:var(--stage)}
  body{position:relative;font-family:"Open Sans",sans-serif;color:var(--white)}
  .card{position:absolute;left:213px;width:774px;height:546px;background:var(--navy);overflow:hidden}
  .card--front{top:40px}
  .card--back{top:613px}

  /* front */
  .front-info{position:absolute;left:0;top:0;width:429px;height:546px;background:var(--navy)}
  .tagline{height:51px;display:flex;align-items:center;padding-left:46px;gap:22px}
  .tagline__main{font-family:"Oswald",sans-serif;font-weight:600;font-size:19px;letter-spacing:.3px}
  .tagline__sub{font-family:"Oswald",sans-serif;font-weight:400;font-size:13px;letter-spacing:.2px}
  .brand-band{height:122px;background:var(--white);display:flex;align-items:center;justify-content:center;gap:10px}
  .brand-mark{width:24px;height:24px;background:var(--accent)}
  .brand-name{font-family:"Oswald",sans-serif;font-weight:400;font-size:19px;letter-spacing:2px;color:var(--ink)}
  .agent-name{font-family:"Oswald",sans-serif;font-weight:600;font-size:42px;letter-spacing:1.2px;line-height:1;text-align:center;text-transform:uppercase;white-space:nowrap}
  .agent-title{font-family:"Oswald",sans-serif;font-weight:300;font-size:22px;line-height:1;text-align:center;margin-top:8px}
  .front-info .agent-block{position:absolute;top:222px;left:0;width:429px}
  .home-row{position:absolute;display:flex}
  .front-info .home-row{top:337px;left:23px;gap:10px}
  .front-info .home{width:120px;height:108px}
  .contact{display:flex;align-items:center;gap:8px;font-size:13px;letter-spacing:.2px;white-space:nowrap}
  .icon{width:18px;height:18px;flex:none}
  .front-contacts{position:absolute;top:467px;left:0;width:429px;display:flex;flex-wrap:wrap;justify-content:center;column-gap:20px;row-gap:14px}
  .front-contacts .contact--web{flex-basis:100%;justify-content:center}
  .front-portrait{position:absolute;right:0;top:0;width:345px;height:546px;background:linear-gradient(90deg,#8a8c8b 0%,#a6a7a5 40%,#7d7f80 100%)}
  .front-portrait::after{content:"";position:absolute;left:34px;right:30px;bottom:0;height:360px;border-radius:120px 120px 0 0;background:linear-gradient(180deg,#1b2a47,#111a2e)}

  /* back */
  .scenery{position:absolute;left:0;top:0;width:463px;height:546px;background:
    radial-gradient(ellipse 38% 40% at 42% 58%,#d3622a 0%,#b5421d 55%,transparent 100%),
    linear-gradient(180deg,#c67067 0%,#b3586a 18%,#2f7fae 40%,#1d6a9b 70%,#0e3e6a 100%)}
  .back-contacts{position:absolute;left:236px;top:446px;display:flex;flex-direction:column;gap:7px}
  .back-panel{position:absolute;left:463px;top:0;width:311px;height:546px;background:var(--navy)}
  .back-portrait{position:absolute;left:70px;top:11px;width:160px;height:202px;background:linear-gradient(180deg,var(--navy) 0%,var(--navy) 45%,#1a2a48 46%,#121c33 100%)}
  .divider{position:absolute;left:0;top:213px;width:311px;height:2px;background:var(--white)}
  .back-panel .agent-block{position:absolute;top:226px;left:0;width:311px}
  .back-panel .agent-name{font-size:32px;letter-spacing:1px}
  .back-panel .agent-title{font-size:19px;margin-top:7px}
  .back-panel .home-row{top:315px;left:17px;gap:12px}
  .back-panel .home{width:128px;height:122px}
  .partner-bar{position:absolute;left:0;top:469px;width:311px;height:46px;background:var(--white);display:flex;align-items:center;justify-content:space-evenly}
  .partner-bar .brand-name{font-size:12px;letter-spacing:1px}
  .partner-bar .brand-mark{width:16px;height:16px}
  .brand-inline{display:flex;align-items:center;gap:6px}
  .badge{width:58px;height:26px;border:2px solid var(--navy-deep);background:#e8eef4}
  .badge--square{width:30px;height:30px;background:var(--ink);border:none}

  .home--modern{background:linear-gradient(160deg,#e8a66a 0%,#5b4a42 50%,#2b2a2e 100%)}
  .home--villa{background:linear-gradient(180deg,#d97a3a 0%,#c79a6a 50%,#3d3028 100%)}
  .home--cottage{background:linear-gradient(180deg,#8fb4d8 0%,#cdb89a 50%,#4f7a3c 100%)}
  .home--pool{background:linear-gradient(180deg,#5aa0d8 0%,#d8d2c4 50%,#2f8fc4 100%)}
  .home--estate{background:linear-gradient(180deg,#7fa8d6 0%,#d9c7a6 55%,#5a8a3a 100%)}
</style>
</head>
<body>
<svg width="0" height="0" style="position:absolute">
  <defs>
    <symbol id="i-mail" viewBox="0 0 18 18"><circle cx="9" cy="9" r="9" fill="#fff"/><rect x="4.5" y="5.8" width="9" height="6.4" fill="#0c4a70"/><path d="M4.5 5.8 9 9.6l4.5-3.8" stroke="#fff" stroke-width="1" fill="none"/></symbol>
    <symbol id="i-phone" viewBox="0 0 18 18"><circle cx="9" cy="9" r="9" fill="#fff"/><path d="M6 4.5c.6-.4 1.2 0 1.5.6l.6 1.4c.2.5 0 .9-.4 1.2l-.5.4c.5 1.1 1.3 1.9 2.3 2.4l.5-.5c.3-.4.8-.5 1.2-.3l1.4.7c.6.3.8.9.5 1.4-.6 1-1.6 1.4-2.7 1-2.6-1-4.5-3-5.4-5.6-.3-1 0-2 1-2.700z" fill="#0c4a70"/></symbol>
    <symbol id="i-web" viewBox="0 0 18 18"><circle cx="9" cy="9" r="9" fill="#fff"/><g fill="none" stroke="#0c4a70" stroke-width="1"><circle cx="9" cy="9" r="4.8"/><ellipse cx="9" cy="9" rx="2" ry="4.8"/><path d="M4.2 9h9.6M5 6.5h8M5 11.5h8"/></g></symbol>
  </defs>
</svg>

<section class="card card--front">
  <div class="front-info">
    <div class="tagline">
      <span class="tagline__main">BUYING ▪ SELLING</span>
      <span class="tagline__sub">ALL YOUR REAL ESTATE NEEDS</span>
    </div>
    <div class="brand-band">
      <span class="brand-mark"></span>
      <span class="brand-name">MESA CREST REALTY</span>
    </div>
    <div class="agent-block">
      <h1 class="agent-name">Brent Holloway</h1>
      <p class="agent-title">REAL ESTATE AGENT</p>
    </div>
    <div class="home-row">
      <div class="home home--modern" role="img" aria-label="Modern home at dusk"></div>
      <div class="home home--villa" role="img" aria-label="Mediterranean villa at sunset"></div>
      <div class="home home--cottage" role="img" aria-label="Craftsman house with garden"></div>
    </div>
    <div class="front-contacts">
      <span class="contact"><svg class="icon"><use href="#i-mail"/></svg>brentholloway@mailvista.net</span>
      <span class="contact"><svg class="icon"><use href="#i-phone"/></svg>(480) 317 4926</span>
      <span class="contact contact--web"><svg class="icon"><use href="#i-web"/></svg>www.Brentholloway.com</span>
    </div>
  </div>
  <div class="front-portrait" role="img" aria-label="Portrait of the agent in a navy suit against a concrete wall"></div>
</section>

<section class="card card--back">
  <div class="scenery" role="img" aria-label="Aerial view of red rock canyon and lake in Arizona"></div>
  <div class="back-contacts">
    <span class="contact"><svg class="icon"><use href="#i-mail"/></svg>brentholloway@mailvista.net</span>
    <span class="contact"><svg class="icon"><use href="#i-phone"/></svg>(480) 317 4926</span>
    <span class="contact"><svg class="icon"><use href="#i-web"/></svg>www.Brentholloway.com</span>
  </div>
  <div class="back-panel">
    <div class="back-portrait" role="img" aria-label="Portrait of the agent in a navy suit"></div>
    <div class="divider"></div>
    <div class="agent-block">
      <h2 class="agent-name">Brent Holloway</h2>
      <p class="agent-title">REAL ESTATE AGENT</p>
    </div>
    <div class="home-row">
      <div class="home home--pool" role="img" aria-label="Modern home with pool overlooking the ocean"></div>
      <div class="home home--estate" role="img" aria-label="Two-storey estate home with lawn"></div>
    </div>
    <div class="partner-bar">
      <span class="brand-inline"><span class="brand-mark"></span><span class="brand-name">MESA CREST REALTY</span></span>
      <span class="badge"></span>
      <span class="badge badge--square"></span>
    </div>
  </div>
</section>
</body>
</html>
```